Brenna Coltrane Electrical would like a flyer to advertise to businesses with our services listed. our website is brennacoltraneelectrical-example.com

Target Market(s)

Businesses and homes

Industry/Entity Type

Electrical

```html
<!DOCTYPE html>
<html lang="en">
<head>
<meta charset="utf-8">
<title>Brenna Coltrane Electrical – Flyer</title>
<link href="https://fonts.googleapis.com/css2?family=Oswald:wght@500;600&family=Tinos&display=swap" rel="stylesheet">
<style>
  :root {
    --ink: #111111;
    --paper: #ffffff;
    --cyan: #66f5ff;
    --lime: #bdf21f;
    --display: "Oswald", "Arial Narrow", sans-serif;
    --body: "Tinos", "Times New Roman", serif;
  }
  * { margin: 0; padding: 0; box-sizing: border-box; }
  html, body { width: 960px; height: 1200px; overflow: hidden; background: var(--paper); }
  .flyer { position: relative; width: 960px; height: 1200px; overflow: hidden; background: var(--paper); color: var(--ink); }

  .brand-square { position: absolute; left: 34px; top: 26px; width: 216px; height: 236px; background: var(--ink); }
  .brand-name {
    position: absolute; left: 266px; top: 22px;
    font-family: var(--display); font-weight: 600; font-size: 98px; line-height: 104px;
    color: var(--ink); white-space: nowrap; letter-spacing: -0.5px;
  }
  .brand-rule { position: absolute; left: 250px; top: 262px; width: 676px; height: 5px; background: var(--ink); }

  .tag {
    position: absolute; display: flex; align-items: center; justify-content: center;
    font-family: var(--display); font-weight: 500; font-size: 70px; color: var(--paper);
    letter-spacing: 0.5px;
  }
  .tag--company { left: 34px; top: 271px; width: 430px; height: 96px; background: var(--cyan); }
  .tag--services { left: 266px; top: 518px; width: 426px; height: 99px; background: var(--lime); }
  .tag--call { left: 602px; top: 766px; width: 326px; height: 98px; background: var(--cyan); }

  .about {
    position: absolute; left: 42px; top: 384px; width: 880px;
    font-family: var(--body); font-size: 17.6px; line-height: 19px; text-align: justify;
    text-indent: 10px;
  }

  .services {
    position: absolute; left: 144px; top: 641px; list-style: none;
    font-family: var(--body); font-size: 22.5px; line-height: 33.6px;
  }
  .services li::before { content: "•"; margin-right: 10px; }

  .backdrop { position: absolute; left: 0; top: 0; }

  .phone {
    position: absolute; right: 30px; top: 1004px;
    font-family: var(--display); font-weight: 600; font-size: 72px; line-height: 80px; color: var(--ink);
  }

  .site-bar {
    position: absolute; left: 0; top: 1102px; width: 960px; height: 98px; background: var(--ink);
    display: flex; align-items: center; justify-content: center;
    font-family: var(--display); font-weight: 500; font-size: 46px; color: var(--paper); white-space: nowrap;
  }
</style>
</head>
<body>
<main class="flyer">
  <svg class="backdrop" width="960" height="1200" viewBox="0 0 960 1200" aria-hidden="true">
    <polygon points="0,894 960,894 960,900 0,1098" fill="var(--cyan)"/>
    <polygon points="960,900 960,1102 120,1102" fill="var(--lime)"/>
    <polygon points="0,1098 330,1032 120,1102 0,1102" fill="var(--paper)"/>
    <rect x="745" y="862" width="36" height="76" fill="var(--cyan)"/>
    <polygon points="706,936 820,936 763,1002" fill="var(--cyan)"/>
  </svg>

  <div class="brand-square" aria-hidden="true"></div>
  <h1 class="brand-name">Brenna Coltrane<br>Electrical</h1>
  <div class="brand-rule"></div>

  <h2 class="tag tag--company">OUR COMPANY</h2>
  <p class="about">Brenna Coltrane Electrical Pty Ltd has over 51 years combined experience in all aspects of the electrical industry. We are committed to being on time and providing exceptional service at all times. We use an automated job tracking system from start to finish on all projects from changing a switch to large projects we have you covered with the latest in service software to ensure all works are streamlined. There is no stress of using contractors when you have us with you.</p>

  <h2 class="tag tag--services">OUR SERVICES</h2>
  <ul class="services">
    <li>Switchboards and Mains Upgrades</li>
    <li>Commercial and Domestic Service and construction</li>
    <li>Lighting Automation, installation and Led Lighting</li>
    <li>Scheduled maintenance</li>
    <li>Lighting Installations</li>
    <li>Power Outlets</li>
    <li>24/7 Emergency Service</li>
  </ul>

  <div class="tag tag--call">CALL NOW</div>
  <div class="phone">0491 570 156</div>

  <footer class="site-bar">Visit us at brennacoltraneelectrical-example.com</footer>
</main>
</body>
</html>
```